Tellwick Asset Management - Corporate Letter Head Project

Looking for a classy design based on our current logo. Please find current logo source file in files. With our color scheme.

Target Market(s)

We're an investment firm, the letterhead needs to look professional and attractive to clients.

Industry/Entity Type

Hedgefund

Colors
0054AA
0677BA
7BADD7
CADEEF
E8F1F8

Requirements
Must have
• Our logo, address, phone number, and email

```html
<!DOCTYPE html>
<html lang="en">
<head>
<meta charset="utf-8">
<title>Tellwick Asset Management — Letterhead</title>
<link href="https://fonts.googleapis.com/css2?family=EB+Garamond:wght@400;500&display=swap" rel="stylesheet">
<style>
  :root {
    --frame: #d4bec1;
    --paper: #ffffff;
    --navy: #163359;
    --steel: #b9c3d2;
    --steel-dark: #8196b0;
    --ink: #163359;
  }
  * { margin: 0; padding: 0; box-sizing: border-box; }
  html, body {
    width: 865px;
    height: 1200px;
    overflow: hidden;
    background: var(--frame);
  }
  .letterhead {
    position: relative;
    width: 865px;
    height: 1200px;
    background: var(--frame);
    font-family: "EB Garamond", "Times New Roman", serif;
  }
  .sheet {
    position: absolute;
    left: 33px;
    top: 35px;
    width: 799px;
    height: 1130px;
    background: var(--paper);
  }
  .shapes {
    position: absolute;
    inset: 0;
    width: 865px;
    height: 1200px;
  }
  .brand {
    position: absolute;
    left: 82px;
    top: 109px;
    display: flex;
    align-items: center;
    gap: 14px;
    color: var(--paper);
  }
  .brand-mark {
    width: 87px;
    height: 87px;
    border: 1.5px solid var(--paper);
  }
  .brand-name {
    display: flex;
    flex-direction: column;
    font-weight: 400;
    line-height: 1;
  }
  .brand-name .line-main {
    font-size: 33px;
    letter-spacing: 0.5px;
  }
  .brand-name .line-sub {
    margin-top: 8px;
    font-size: 20px;
    letter-spacing: 15.6px;
  }
  .contact {
    position: absolute;
    list-style: none;
    color: var(--ink);
    font-size: 15px;
  }
  .contact li {
    position: absolute;
    display: flex;
    align-items: center;
    gap: 12px;
    white-space: nowrap;
  }
  .contact .icon {
    width: 26px;
    height: 26px;
    border-radius: 50%;
    background: var(--navy);
    display: flex;
    align-items: center;
    justify-content: center;
  }
  .contact-address { left: 560px; top: 100px; }
  .contact-phone   { left: 579px; top: 132px; }
  .contact-email   { left: 598px; top: 163px; }
  .website {
    position: absolute;
    left: 50px;
    top: 1112px;
    font-size: 18.5px;
    color: var(--ink);
    letter-spacing: 0.2px;
  }
</style>
</head>
<body>
<div class="letterhead">
  <div class="sheet"></div>

  <svg class="shapes" viewBox="0 0 865 1200" aria-hidden="true">
    <!-- header -->
    <polygon points="481,83 500,56 516,83" fill="var(--steel-dark)"/>
    <polygon points="500,56 832,56 832,222 597,222" fill="var(--steel)"/>
    <polyline points="832,63.5 514,63.5 602,214 832,214" fill="none" stroke="#ffffff" stroke-width="0.8"/>
    <polygon points="33,83 516,83 592,213 33,213" fill="var(--navy)"/>
    <!-- footer -->
    <polygon points="359,1135.5 370,1135.5 365,1144" fill="var(--steel-dark)"/>
    <polygon points="347,1110 832,1110 832,1135.5 362,1135.5" fill="var(--navy)"/>
    <polygon points="33,1104 344,1104 365,1144 33,1144" fill="var(--steel)"/>
  </svg>

  <div class="brand">
    <div class="brand-mark"></div>
    <div class="brand-name">
      <span class="line-main">TELLWICK ASSET</span>
      <span class="line-sub">MANAGEMENT</span>
    </div>
  </div>

  <ul class="contact">
    <li class="contact-address">
      <span class="icon">
        <svg width="14" height="14" viewBox="0 0 14 14"><path d="M1.5 6.5 L7 2.5 L12.5 6.5" fill="none" stroke="#fff" stroke-width="1.4"/><path d="M3.5 7 V12 H6 V9.5 H8 V12 H10.5 V7 L7 4.5 Z" fill="#fff"/></svg>
      </span>
      <span>address/office</span>
    </li>
    <li class="contact-phone">
      <span class="icon">
        <svg width="14" height="14" viewBox="0 0 14 14"><path d="M3.2 1.5 L5 3.8 L4 5.3 C4.8 7 6.5 8.8 8.5 9.8 L10 8.8 L12.3 10.6 L11 12.5 C6.5 12 2.2 7.5 1.6 3 Z" fill="#fff"/></svg>
      </span>
      <span>phone number</span>
    </li>
    <li class="contact-email">
      <span class="icon">
        <svg width="16" height="12" viewBox="0 0 16 12"><rect x="1" y="1.5" width="14" height="9" fill="none" stroke="#fff" stroke-width="1.2"/><path d="M1 1.5 L8 7 L15 1.5 M1 10.5 L6 6 M15 10.5 L10 6" fill="none" stroke="#fff" stroke-width="1.1"/></svg>
      </span>
      <span>email</span>
    </li>
  </ul>

  <div class="website">www.tellwickassetmanagement.com</div>
</div>
</body>
</html>
```